Design a double sided business card

We are looking for a clean, eye-catching, and contemporary design that enhances the brand and presents a premium, professional image. Our preference is for a brown card with black gloss detailing and embossed elements; however, we are open to creative input and design suggestions that best achieve a strong visual impact.

Please see the attached existing business card for reference. We use both black and brown colours consistently across our branding.

On sample provided

```html
<!DOCTYPE html>
<html lang="en">
<head>
<meta charset="utf-8">
<title>Kestrel – Business Card</title>
<link rel="stylesheet" href="https://fonts.googleapis.com/css2?family=Exo+2:ital,wght@0,300;0,400;0,600;0,700;1,400&display=swap">
<style>
  :root {
    --backdrop: #d8d8d8;
    --tan: #c8b497;
    --ink: #000000;
    --photo-light: #e6dccb;
    --photo-mid: #a8957a;
    --photo-dark: #3e3428;
    --rule: #1a1a1a;
  }
  * { box-sizing: border-box; margin: 0; padding: 0; }
  html, body {
    width: 1200px; height: 848px; overflow: hidden;
    background: var(--backdrop);
    font-family: "Exo 2", sans-serif;
  }
  .canvas { position: relative; width: 1200px; height: 848px; }

  .card {
    position: absolute; top: 275px;
    width: 520px; height: 297px;
  }

  /* Front side */
  .card-front { left: 50px; background: var(--tan); padding: 14px; }
  .front-panel {
    position: relative; width: 100%; height: 100%;
    background: var(--ink);
  }
  .brand-lockup {
    position: absolute; left: 30px; top: 100px; width: 205px;
    display: flex; flex-direction: column; align-items: center; gap: 14px;
  }
  .brand-square { width: 58px; height: 58px; background: var(--tan); }
  .brand-name {
    color: var(--tan); font-weight: 700; font-size: 27px;
    letter-spacing: 3px; line-height: 1;
  }
  .brand-rule {
    position: absolute; left: 34px; top: 215px; width: 210px; height: 1px;
    background: var(--rule);
  }
  .contact {
    position: absolute; left: 253px; top: 36px; color: var(--tan);
  }
  .contact-name { font-weight: 700; font-size: 24px; line-height: 1.1; }
  .contact-role {
    font-style: italic; font-size: 12px; letter-spacing: 3px;
    margin-top: 2px; margin-bottom: 16px;
  }
  .contact-block { font-weight: 300; font-size: 15px; line-height: 20px; }
  .contact-block + .contact-block { margin-top: 12px; }
  .contact-lines { font-weight: 300; font-size: 15px; line-height: 23px; }

  /* Back side */
  .card-back { left: 630px; background: var(--ink); padding: 14px; }
  .back-photo {
    position: relative; width: 100%; height: 100%;
    background: radial-gradient(ellipse at 50% 45%, var(--photo-light) 0%, var(--photo-mid) 55%, var(--photo-dark) 100%);
  }
  .back-brand {
    position: absolute; top: 22px; left: 0; right: 0; text-align: center;
    color: var(--ink); font-weight: 700; font-size: 22px; letter-spacing: 3px;
  }
  .web-tab { position: absolute; left: 50%; bottom: 0; transform: translateX(-50%); }
  .web-tab svg { display: block; }
  .web-tab-text {
    position: absolute; inset: 0; display: flex; align-items: center; justify-content: center;
    color: var(--photo-light); font-size: 12px; font-weight: 600; letter-spacing: 1.5px;
    padding-top: 2px;
  }
</style>
</head>
<body>
<main class="canvas">

  <section class="card card-front" aria-label="Business card front">
    <div class="front-panel">
      <div class="brand-lockup">
        <span class="brand-square"></span>
        <span class="brand-name">KESTREL</span>
      </div>
      <span class="brand-rule"></span>
      <div class="contact">
        <p class="contact-name">Theo Marsh</p>
        <p class="contact-role">DIRECTOR</p>
        <p class="contact-block">The Old Mill Orchard Lane<br>Ashford TN24 8QR</p>
        <div class="contact-block contact-lines">
          <p>Phone: 0800 555 0142</p>
          <p>Mobile: 0770 0900 1234</p>
          <p>Email: theo@kestrelhomes.co.uk</p>
          <p>www.kestrelhomes.co.uk</p>
        </div>
      </div>
    </div>
  </section>

  <section class="card card-back" aria-label="Business card back">
    <div class="back-photo" role="img" aria-label="Sepia-toned photograph of a modern glass-walled living room with a long sofa and armchairs">
      <p class="back-brand">KESTREL</p>
      <div class="web-tab">
        <svg width="200" height="24" viewBox="0 0 200 24" aria-hidden="true">
          <polygon points="12,0 188,0 200,24 0,24" fill="#000"/>
        </svg>
        <span class="web-tab-text">WWW.KESTRELHOMES.CO.UK</span>
      </div>
    </div>
  </section>

</main>
</body>
</html>
```